Brochure for Security Guard and Video Monitoring Services

I need a brochure design so I can hand our brochures to prospects at a trade show. I will provide my company logo and some content and a few pictures to put into the brochure design. I am open to you adding other stock photos if you feel it can help the look of the brochure. Logo provided in .png and .eps

Industry/Entity Type

It Company

Requirements
Must have
• Few photos.

```html
<!DOCTYPE html>
<html lang="en">
<head>
<meta charset="utf-8">
<title>Ridgeline Group – Video Monitoring Brochure</title>
<link href="https://fonts.googleapis.com/css2?family=Arimo:wght@400;700&family=Caladea&display=swap" rel="stylesheet">
<style>
  :root{
    --backdrop:#dcdcdf;
    --paper:#f1f1f4;
    --heading-blue:#2f8fc9;
    --sub-navy:#2b2f7e;
    --ink:#222226;
    --wave-deep:#2a83c4;
    --wave-mid:#4a9bd3;
    --wave-light:#b9d4ec;
    --fold:#d6d6dc;
  }
  *{box-sizing:border-box;margin:0;padding:0}
  html,body{width:1200px;height:942px;overflow:hidden;background:var(--backdrop)}
  body{font-family:"Arimo",Arial,sans-serif;color:var(--ink)}
  .spread{position:absolute;left:80px;top:71px;width:1040px;height:800px;background:var(--paper);overflow:hidden;box-shadow:0 6px 18px rgba(0,0,0,.18)}
  .fold{position:absolute;left:520px;top:0;width:1px;height:100%;background:var(--fold)}
  .wave{position:absolute;left:0;bottom:0;width:1040px;height:260px}
  .page{position:absolute;top:0;width:520px;height:100%}
  .page-left{left:0;padding:42px 40px 0 44px}
  .page-right{left:520px;padding:30px 40px 0 42px}
  .section-title{font-family:"Caladea",Cambria,serif;font-weight:400;font-size:27px;color:var(--heading-blue);line-height:1.1}
  .intro{font-size:14.5px;line-height:25px;text-align:justify;margin-top:8px;text-indent:30px}
  .advantages-title{margin-top:14px}
  .benefit{margin-top:10px}
  .benefit-title{font-weight:700;font-size:17px;color:var(--sub-navy);letter-spacing:.2px}
  .page-right .benefit-title{font-size:17px}
  .benefit-text{font-size:17px;line-height:26px;margin-top:14px;text-align:justify}
  .page-right .benefit-text{font-size:16px;line-height:25px;margin-top:10px}
  .tick{display:inline-block;width:10px;height:10px;margin:0 18px 0 2px;vertical-align:1px}
  .closing{font-size:13.8px;line-height:25px;margin-top:14px;text-align:justify;position:relative;z-index:2}
  .camera-photo{position:absolute;left:330px;top:560px;width:160px;height:240px;background:linear-gradient(180deg,#e6e6ea 0%,#b9bcc2 55%,#3a3d44 100%);z-index:1}
  .page-left,.page-right{z-index:2}
</style>
</head>
<body>
<main class="spread">
  <svg class="wave" viewBox="0 0 1040 260" preserveAspectRatio="none" aria-hidden="true">
    <path d="M0 40 C200 70 380 150 560 140 C760 130 900 60 1040 40 L1040 260 L0 260 Z" fill="var(--wave-light)"/>
    <path d="M0 70 C220 110 380 190 560 175 C760 160 900 90 1040 70 L1040 260 L0 260 Z" fill="var(--wave-mid)"/>
    <path d="M0 95 C220 140 400 220 580 200 C780 180 910 120 1040 100 L1040 260 L0 260 Z" fill="var(--wave-deep)"/>
  </svg>
  <div class="fold"></div>
  <div class="camera-photo" role="img" aria-label="Photo of security cameras mounted on a pole"></div>

  <section class="page page-left">
    <h1 class="section-title">About Us</h1>
    <p class="intro">Ridgeline Group offers remove live video monitoring. This program has some key advantages for some customers. We use high quality components to monitor your site remotely and respond to analytic based alarms. Our in-house operators verify all alarms and communicate via loudspeaker with intruders while co-ordinating security and police response.</p>

    <h2 class="section-title advantages-title">Advantages</h2>
    <div class="benefit">
      <h3 class="benefit-title">Save money</h3>
      <p class="benefit-text"><svg class="tick" viewBox="0 0 10 10" aria-hidden="true"><path d="M1 5 L4 8 L9 1" fill="none" stroke="#222" stroke-width="2"/></svg>Can be half the cost of a security guard</p>
    </div>
    <div class="benefit">
      <h3 class="benefit-title">Theft reduction</h3>
      <p class="benefit-text"><svg class="tick" viewBox="0 0 10 10" aria-hidden="true"><path d="M1 5 L4 8 L9 1" fill="none" stroke="#222" stroke-width="2"/></svg>Cameras and signage deter theft. Live operator speaking to intruder stops thefts.</p>
    </div>
    <div class="benefit">
      <h3 class="benefit-title">Flat Monthly Fee</h3>
      <p class="benefit-text"><svg class="tick" viewBox="0 0 10 10" aria-hidden="true"><path d="M1 5 L4 8 L9 1" fill="none" stroke="#222" stroke-width="2"/></svg>Monthly fee is all inclusive of all equipment; setup; monitoring; troubleshooting</p>
    </div>
  </section>

  <section class="page page-right">
    <div class="benefit">
      <h3 class="benefit-title">Several Set of Eyes</h3>
      <p class="benefit-text"><svg class="tick" viewBox="0 0 10 10" aria-hidden="true"><path d="M1 5 L4 8 L9 1" fill="none" stroke="#222" stroke-width="2"/></svg>Having several cameras with analytics is like having several security staff posted at various positions at all times on your property.</p>
    </div>
    <div class="benefit">
      <h3 class="benefit-title">Timely Police Response</h3>
      <p class="benefit-text"><svg class="tick" viewBox="0 0 10 10" aria-hidden="true"><path d="M1 5 L4 8 L9 1" fill="none" stroke="#222" stroke-width="2"/></svg>With a verified crime in progress the police will respond much quicker</p>
    </div>
    <div class="benefit">
      <h3 class="benefit-title">Continuous Video Recording</h3>
      <p class="benefit-text"><svg class="tick" viewBox="0 0 10 10" aria-hidden="true"><path d="M1 5 L4 8 L9 1" fill="none" stroke="#222" stroke-width="2"/></svg>System can be set to record 24/7 to ensure evidence of incidents are available</p>
    </div>
    <div class="benefit">
      <h3 class="benefit-title">Flexibility</h3>
      <p class="benefit-text"><svg class="tick" viewBox="0 0 10 10" aria-hidden="true"><path d="M1 5 L4 8 L9 1" fill="none" stroke="#222" stroke-width="2"/></svg>System can be set up in environments where no power is available by using solar and batteries.</p>
      <p class="benefit-text"><svg class="tick" viewBox="0 0 10 10" aria-hidden="true"><path d="M1 5 L4 8 L9 1" fill="none" stroke="#222" stroke-width="2"/></svg>System can be moved and altered as projects change and evolve</p>
    </div>
    <p class="closing">All aspects of our video monitoring is managed in house. Installation, video monitoring; mobile responses are all in house. We do not outsource anything which ensures we provide the highest level of service to our customers.</p>
  </section>
</main>
</body>
</html>
```